Hardcore nerd needs to stand out in a sea of dull Defence business cards

Wombat Devices is a new Australian consulting engineering company that turns research and theory into practical systems. No evangelistic fluff, just mathematics and physics into electronic and optical circuits for consumer products, scientific research or Defence applications.

We already have a recognised logo (provided) which is often dark blue/black on a light background but we're open to other combinations. (Us engineers tend to have limited aesthetic imagination :)

Some of our recent products have included:
* Instrumentation for electrical testing,
* Radar jammers,
* GPS antenna design,
* Satellite tracking systems,
* High power lasers

We're open to both single and double-sided designs - happy to be convinced either way.

P.S. Another group is working on the web page, so - alas - our web site is currently of no use for images/ideas...

Target Market(s)

Engineering managers,
Scientists

Contact Information for Business Card

Dr Colin Marsh
R&D Engineer

colin@wombatdevicesco.com.au
0427 563 210

PO Box XXX (to be confirmed)
Banks ACT 2913
Australia

Font styles to use
Serif
Sans Serif

Colors

Designer to choose colors to be used in the design.

Requirements
Must have
• My contact details!
• I've had many (great) "bold and plain" designs submitted already, so feel free to be artistically creative :)
• Happy to take advice re fonts/colours/printability etc.
Nice to have
• I'm not sure if "lists" are more at home on a CV than a business card, but representative services include:
• Applied electromagnetics
• RF and high speed electronics
• Signal and image processing
• Electro-optical and laser systems
• Concept-to-prototype design services
• If you're considering double sided cards, then often measuring/alignment grids/rulers feature on the back of similar cards.
• e.g. https://www.lumoptix-example.com/newgrouppage9.cfm?objectgroup_id=4815
• https://www.lumoptix-example.com/newgrouppage9.cfm?objectgroup_ID=4817
• ..or even a "Smith chart" (google will return lots)
• Generic images to represent a capability might work - googling images associated with keyword for each of these areas might help:
• - "passive radar", "phased array", "fdtd", "vircator"
• RF and high speed electronic design
• - "smith chart", "microstrip circuits", "dimensioned drawing", "electronic schematic"
• - "dft", "iir filter"
• - "optical cavity". "laser energy level diagram"
• Background/watermarked images outlines/wireframes/schematics would probably look OK.
Should not have
• If a list of projects/services is provided, it is important not to make the client feel that this is "all" the company can do. Engineering design is a creative discipline (like graphics :)
• Please, no stock "military" snaps like planes, missiles, etc!

```html
<!DOCTYPE html>
<html lang="en">
<head>
<meta charset="utf-8">
<title>Wombat Devices – Business Card</title>
<link href="https://fonts.googleapis.com/css2?family=Montserrat:wght@500;600;700;800&display=swap" rel="stylesheet">
<style>
  :root {
    --backdrop: #2e2e30;
    --navy: #1b2262;
    --navy-deep: #10164a;
    --navy-mid: #1d2a78;
    --blue-bright: #2f4bc0;
    --blue-glow: #3a5ad6;
    --paper: #f3f3f1;
    --white: #ffffff;
  }
  * { margin: 0; padding: 0; box-sizing: border-box; }
  html, body {
    width: 1200px; height: 901px; overflow: hidden;
    background: var(--backdrop);
    font-family: "Montserrat", sans-serif;
  }
  .card {
    position: absolute; left: 320px;
    width: 560px; height: 320px;
    overflow: hidden;
  }

  /* Back of card */
  .card-back { top: 80px; }
  .card-back .pattern-field {
    position: absolute; inset: 0;
    background:
      radial-gradient(ellipse 70% 80% at 95% 95%, var(--blue-glow) 0%, rgba(58, 90, 214, 0) 70%),
      radial-gradient(ellipse 60% 70% at 10% 10%, var(--navy-deep) 0%, rgba(16, 22, 74, 0) 75%),
      linear-gradient(125deg, var(--navy-deep) 0%, var(--navy-mid) 50%, var(--blue-bright) 100%);
  }
  .card-back .lockup {
    position: absolute; left: 290px; top: 130px;
    display: flex; align-items: center; gap: 12px;
    color: var(--white);
  }
  .lockup-dot {
    width: 56px; height: 56px; border-radius: 50%;
    background: currentColor; flex: none;
  }
  .lockup-name { font-weight: 700; line-height: 1; }
  .lockup-name .word-main { display: block; font-size: 25px; letter-spacing: 1px; }
  .lockup-name .word-sub { display: block; font-size: 12px; letter-spacing: 5.5px; margin-top: 5px; }

  /* Front of card */
  .card-front { top: 470px; background: var(--paper); color: var(--navy); }
  .card-front .lockup {
    position: absolute; left: 130px; top: 46px;
    display: flex; align-items: center; gap: 16px;
  }
  .card-front .lockup-dot { width: 90px; height: 90px; }
  .card-front .lockup-name .word-main { font-size: 36px; letter-spacing: 1.5px; }
  .card-front .lockup-name .word-sub { font-size: 17px; letter-spacing: 8px; margin-top: 7px; }

  .person {
    position: absolute; right: 300px; top: 190px; text-align: right;
  }
  .person-name { font-size: 19px; font-weight: 800; letter-spacing: 0.4px; }
  .person-role { font-size: 15px; font-weight: 500; margin-top: 3px; }
  .divider {
    position: absolute; left: 274px; top: 192px;
    width: 2px; height: 74px; background: var(--navy);
  }
  .contact {
    position: absolute; left: 290px; top: 190px;
    font-size: 12px; font-weight: 500; line-height: 1.5;
  }
  .contact-line { display: flex; align-items: center; gap: 6px; }
  .contact-line svg { width: 11px; height: 11px; fill: var(--navy); flex: none; }
  .contact-address { margin-top: 3px; }
</style>
</head>
<body>
  <section class="card card-back">
    <div class="pattern-field" role="img" aria-label="Tone-on-tone embossed repeat pattern across a deep navy to bright blue ground"></div>
    <div class="lockup">
      <span class="lockup-dot"></span>
      <span class="lockup-name">
        <span class="word-main">WOMBAT</span>
        <span class="word-sub">DEVICES</span>
      </span>
    </div>
  </section>

  <section class="card card-front">
    <div class="lockup">
      <span class="lockup-dot"></span>
      <span class="lockup-name">
        <span class="word-main">WOMBAT</span>
        <span class="word-sub">DEVICES</span>
      </span>
    </div>

    <div class="person">
      <div class="person-name">DR COLIN MARSH</div>
      <div class="person-role">R&amp;D Engineer</div>
    </div>

    <div class="divider"></div>

    <div class="contact">
      <div class="contact-line">
        <svg viewBox="0 0 24 24" aria-hidden="true"><path d="M6.6 10.8a15.1 15.1 0 0 0 6.6 6.6l2.2-2.2c.3-.3.7-.4 1-.2 1.1.4 2.3.6 3.6.6.6 0 1 .4 1 1V20c0 .6-.4 1-1 1A17 17 0 0 1 3 4c0-.6.4-1 1-1h3.5c.6 0 1 .4 1 1 0 1.3.2 2.5.6 3.6.1.3 0 .7-.2 1z"/></svg>
        <span>0427 563 210</span>
      </div>
      <div class="contact-line">
        <svg viewBox="0 0 24 24" aria-hidden="true"><path d="M2 5h20v14H2zm2 2v.5l8 5 8-5V7zm0 2.9V17h16V9.9l-8 5z"/></svg>
        <span>colin@wombatdevicesco.com.au</span>
      </div>
      <div class="contact-address">PO Box XXX<br>Banks ACT 2913, Australia</div>
    </div>
  </section>
</body>
</html>
```